Brisk Bowl all natural shake full body sleeve design label

We need a label design for a new product launch of Brisk Bowl whole body nutrition shake. Full body sleeve shrink. We have uploaded a brief in pdf format to review with most details. Thank you in advance for your consideration.

The Pelican Grove logo is our company logo, which will be small somewhere on the back / side of bottle where company info will be. Just thought it might spark something creative.

Industry/Entity Type

Nutrition

```html
<!DOCTYPE html>
<html lang="en">
<head>
<meta charset="utf-8">
<title>Brisk Bowl Whole Body Nutritional Shake Label</title>
<link href="https://fonts.googleapis.com/css2?family=Roboto+Condensed:wght@400;700&display=swap" rel="stylesheet">
<style>
  :root {
    --bg: #ffffff;
    --green-dark: #4f8a2b;
    --green-light: #8cc63f;
    --brown: #5b3a29;
    --brown-light: #8a6552;
    --brown-deep: #3b1d12;
    --purple: #7a2b92;
    --magenta: #c4167f;
    --orange: #f27521;
    --orange-light: #f7931e;
    --yellow: #f9d21c;
    --leaf-purple: #7d2a94;
    --leaf-green: #8dc63f;
  }
  html, body {
    margin: 0;
    padding: 0;
    width: 927px;
    height: 1200px;
    overflow: hidden;
    background: var(--bg);
  }
  .label {
    position: relative;
    width: 927px;
    height: 1200px;
    font-family: "Roboto Condensed", "Arial Narrow", sans-serif;
  }
  .label-art {
    position: absolute;
    inset: 0;
  }
  .leaf-pair {
    position: absolute;
    left: 106px;
    top: 133px;
    width: 115px;
    height: 340px;
    border-radius: 60% 40% 55% 45% / 35% 30% 40% 35%;
    background: linear-gradient(180deg, var(--leaf-purple) 0%, var(--leaf-purple) 52%, var(--leaf-green) 62%, var(--leaf-green) 100%);
  }
  .t { font-family: "Roboto Condensed", "Arial Narrow", sans-serif; }
  .t-head { font-weight: 700; font-size: 20px; }
  .t-bold { font-weight: 700; }
  .fill-brown { fill: var(--brown); }
  .fill-brown-light { fill: var(--brown-light); }
  .fill-deep { fill: var(--brown-deep); }
  .fill-green { fill: var(--green-dark); }
  .band { fill: var(--green-light); }
  .icon { fill: #ffffff; }
  .icon-line { stroke: #ffffff; stroke-width: 3; fill: none; }
  .stop-green-dark { stop-color: var(--green-dark); }
  .stop-green-light { stop-color: var(--green-light); }
  .stop-brown { stop-color: var(--brown); }
  .stop-brown-light { stop-color: var(--brown-light); }
  .stop-purple { stop-color: var(--purple); }
  .stop-magenta { stop-color: var(--magenta); }
  .stop-orange { stop-color: var(--orange); }
  .stop-orange-light { stop-color: var(--orange-light); }
  .stop-yellow { stop-color: var(--yellow); }
</style>
</head>
<body>
<div class="label">
  <div class="leaf-pair" role="img" aria-label="Illustration of a purple leaf above a green leaf"></div>

  <svg class="label-art" width="927" height="1200" viewBox="0 0 927 1200" xmlns="http://www.w3.org/2000/svg">
    <defs>
      <linearGradient id="grad-benefits" x1="0" y1="0" x2="0" y2="1">
        <stop offset="0" class="stop-green-dark"/><stop offset="1" class="stop-green-light"/>
      </linearGradient>
      <linearGradient id="grad-brown" x1="0" y1="0" x2="0" y2="1">
        <stop offset="0" class="stop-brown"/><stop offset="1" class="stop-brown-light"/>
      </linearGradient>
      <linearGradient id="grad-fruits" x1="0" y1="0" x2="1" y2="0">
        <stop offset="0" class="stop-purple"/><stop offset="1" class="stop-purple"/>
      </linearGradient>
      <linearGradient id="grad-vitamins" x1="0" y1="0" x2="1" y2="0">
        <stop offset="0" class="stop-purple"/><stop offset="1" class="stop-magenta"/>
      </linearGradient>
      <linearGradient id="grad-antiox" x1="0" y1="0" x2="0" y2="1">
        <stop offset="0" class="stop-orange"/><stop offset="1" class="stop-orange-light"/>
      </linearGradient>
      <linearGradient id="grad-probiotics" x1="0" y1="0" x2="0" y2="1">
        <stop offset="0" class="stop-orange-light"/><stop offset="1" class="stop-yellow"/>
      </linearGradient>
      <linearGradient id="grad-digestive" x1="0" y1="0" x2="1" y2="0">
        <stop offset="0" class="stop-purple"/><stop offset="1" class="stop-purple"/>
      </linearGradient>
      <linearGradient id="grad-immune" x1="0" y1="0" x2="1" y2="0">
        <stop offset="0" class="stop-magenta"/><stop offset="1" class="stop-magenta"/>
      </linearGradient>
    </defs>

    <!-- product header -->
    <text class="t t-head fill-deep" x="486" y="40" text-anchor="middle" textLength="320" lengthAdjust="spacingAndGlyphs">WHOLE BODY NUTRITIONAL SHAKE</text>
    <text class="t t-head fill-brown" x="486" y="64" text-anchor="middle" textLength="320" lengthAdjust="spacingAndGlyphs">CREAMY DARK CHOCOLATE GELATO</text>

    <!-- benefit list -->
    <text class="t t-bold" fill="url(#grad-benefits)" x="234" y="261" font-size="180" textLength="502" lengthAdjust="spacingAndGlyphs">BENEFITS</text>
    <text class="t fill-deep" x="233" y="308" font-size="48" textLength="503" lengthAdjust="spacingAndGlyphs">16 GRAMS OF NON-GMO PEA PROTEIN</text>
    <text class="t" fill="url(#grad-brown)" x="231" y="375" font-size="70" textLength="505" lengthAdjust="spacingAndGlyphs">2 GRAMS DIETARY FIBER</text>
    <text class="t" fill="url(#grad-fruits)" x="231" y="445" font-size="70" textLength="505" lengthAdjust="spacingAndGlyphs">FRUITS &amp; VEGETABLES</text>
    <text class="t" fill="url(#grad-vitamins)" x="231" y="513" font-size="70" textLength="505" lengthAdjust="spacingAndGlyphs">VITAMINS &amp; MINERALS</text>
    <text class="t" fill="url(#grad-antiox)" x="231" y="613" font-size="112" textLength="505" lengthAdjust="spacingAndGlyphs">ANTIOXIDANTS</text>
    <text class="t" fill="url(#grad-probiotics)" x="231" y="733" font-size="140" textLength="505" lengthAdjust="spacingAndGlyphs">PROBIOTICS</text>
    <text class="t" fill="url(#grad-digestive)" x="231" y="808" font-size="87" textLength="505" lengthAdjust="spacingAndGlyphs">DIGESTIVE ENZYMES</text>
    <text class="t" fill="url(#grad-immune)" x="231" y="888" font-size="90" textLength="505" lengthAdjust="spacingAndGlyphs">IMMUNE SUPPORT</text>
    <text class="t fill-deep" x="231" y="986" font-size="105" textLength="505" lengthAdjust="spacingAndGlyphs">LIVER SUPPORT</text>
    <text class="t fill-brown" x="231" y="1036" font-size="50" textLength="505" lengthAdjust="spacingAndGlyphs">ACHES-PAIN-STIFFNESS SUPPORT</text>
    <text class="t fill-brown-light" x="234" y="1085" font-size="45" textLength="502" lengthAdjust="spacingAndGlyphs">ALL NATURAL PLANT BASED VEGETARIAN</text>

    <!-- free-from band -->
    <rect class="band" x="306" y="1103" width="430" height="75"/>
    <rect fill="#ffffff" x="306" y="1103" width="12" height="75"/>
    <text class="t fill-green" x="234" y="1174" font-size="95" textLength="80" lengthAdjust="spacingAndGlyphs">NO</text>

    <!-- dairy -->
    <path class="icon" d="M344 1118 h14 v8 l5 8 v26 h-24 v-26 l5 -8 z"/>
    <!-- sugar cube -->
    <path class="icon" d="M408 1122 l18 9 v20 l-18 9 l-18 -9 v-20 z"/>
    <!-- wheat -->
    <g class="icon">
      <rect x="459.5" y="1118" width="3" height="44"/>
      <ellipse cx="455" cy="1128" rx="3" ry="6"/><ellipse cx="467" cy="1128" rx="3" ry="6"/>
      <ellipse cx="455" cy="1140" rx="3" ry="6"/><ellipse cx="467" cy="1140" rx="3" ry="6"/>
      <ellipse cx="461" cy="1118" rx="3" ry="5"/>
    </g>
    <!-- soy pod -->
    <g class="icon">
      <circle cx="503" cy="1127" r="8"/><circle cx="513" cy="1140" r="8"/><circle cx="523" cy="1153" r="8"/>
    </g>
    <!-- flask -->
    <path class="icon-line" d="M568 1118 h12 M571 1118 v14 l-12 26 h30 l-12 -26 v-14"/>
    <!-- beans -->
    <g class="icon">
      <ellipse cx="629" cy="1130" rx="9" ry="7"/><ellipse cx="647" cy="1131" rx="9" ry="7"/>
      <ellipse cx="630" cy="1148" rx="9" ry="7"/><ellipse cx="648" cy="1149" rx="9" ry="7"/>
    </g>
    <!-- drop -->
    <path class="icon" d="M698 1118 c-4 10 -12 20 -12 29 a12 12 0 0 0 24 0 c0 -9 -8 -19 -12 -29 z"/>

    <!-- servings and calories -->
    <text class="t t-bold fill-deep" x="174" y="1143" font-size="30" text-anchor="middle">30</text>
    <text class="t fill-brown" x="174" y="1159" font-size="12" text-anchor="middle">SERVINGS</text>
    <text class="t t-bold fill-deep" x="798" y="1143" font-size="30" text-anchor="middle">116</text>
    <text class="t fill-brown" x="798" y="1159" font-size="12" text-anchor="middle">CALORIES</text>
  </svg>
</div>
</body>
</html>
```